Design new marketing postcard for mortgage loan applicants

I have provided a postcard recently designed as a possible guide for this project and have attached it. The new text is rough drafted and included. Please feel free to design outside of the old postcard or you can design close to it.

```html
<!DOCTYPE html>
<html lang="en">
<head>
<meta charset="utf-8">
<title>Crestline Home Lending – Cash Out Equity Loan Postcard</title>
<link rel="stylesheet" href="https://fonts.googleapis.com/css2?family=Montserrat:wght@600;700;800;900&family=Poppins:wght@600;700&family=Open+Sans:wght@400;600;700&display=swap">
<style>
  :root {
    --navy: #13284a;
    --gold: #c9962a;
    --gold-light: #e6c15c;
    --red: #d3202a;
    --ink: #1c1c1c;
    --rule: #9a9a9a;
    --white: #ffffff;
    --page: #ffffff;
  }
  * { box-sizing: border-box; margin: 0; padding: 0; }
  html, body { width: 927px; height: 1200px; overflow: hidden; background: var(--page); }
  body { position: relative; font-family: "Open Sans", Arial, sans-serif; color: var(--ink); }

  .postcard {
    position: absolute;
    left: 125px;
    width: 675px;
    background: var(--white);
    overflow: hidden;
    box-shadow: 0 3px 10px rgba(0,0,0,0.28);
  }
  .postcard--front { top: 110px; height: 482px; }
  .postcard--back { top: 624px; height: 471px; }

  .card-art { position: absolute; inset: 0; width: 100%; height: 100%; }

  /* Brand lockup */
  .brand {
    position: absolute;
    display: flex;
    align-items: center;
    gap: 12px;
  }
  .brand__mark {
    width: 50px; height: 50px;
    border-radius: 50%;
    background: var(--gold);
    flex: none;
  }
  .brand__name {
    font-family: "Open Sans", Arial, sans-serif;
    font-weight: 700;
    font-size: 18px;
    line-height: 20px;
    color: var(--navy);
    white-space: nowrap;
  }

  /* Call bars */
  .call-tag {
    background: var(--red);
    color: var(--white);
    font-family: "Montserrat", Arial, sans-serif;
    font-weight: 600;
    white-space: nowrap;
  }
  .call-number {
    font-family: "Poppins", Arial, sans-serif;
    font-weight: 700;
    color: var(--white);
    white-space: nowrap;
  }

  /* Front */
  .hero-photo {
    position: absolute;
    left: 374px; top: 0;
    width: 301px; height: 395px;
    background: radial-gradient(ellipse at 55% 45%, #e9c7ad 0%, #b98f70 35%, #4e7fae 70%, #2d5680 100%);
  }
  .headline {
    position: absolute;
    left: 54px; top: 36px;
    width: 340px;
    text-align: center;
    color: var(--navy);
  }
  .headline__main {
    font-family: "Montserrat", Arial, sans-serif;
    font-weight: 900;
    font-size: 42px;
    line-height: 42px;
    letter-spacing: -1.5px;
  }
  .headline__sub {
    margin-top: 6px;
    font-family: "Montserrat", Arial, sans-serif;
    font-weight: 700;
    font-size: 13.5px;
    letter-spacing: 1.6px;
  }
  .benefits {
    position: absolute;
    left: 78px; top: 205px;
    list-style: none;
    font-size: 16px;
    line-height: 18.5px;
  }
  .benefits li { display: flex; align-items: center; gap: 7px; white-space: nowrap; }
  .benefits svg { width: 12px; height: 12px; flex: none; }

  .nmls {
    position: absolute;
    left: 230px; top: 316px;
    font-size: 12px;
  }
  .postcard--front .brand { left: 100px; top: 334px; }

  .call-bar {
    position: absolute;
    left: 0; bottom: 0;
    width: 100%; height: 87px;
    background: var(--navy);
    border-top: 5px solid var(--gold);
    display: flex;
    align-items: center;
    gap: 28px;
    padding-left: 102px;
  }
  .call-bar .call-tag {
    font-size: 22px;
    letter-spacing: 4px;
    line-height: 42px;
    width: 102px;
    text-align: center;
  }
  .call-bar .call-number { font-size: 46px; line-height: 50px; }

  /* Back */
  .postcard--back .brand { left: 92px; top: 34px; }
  .letter {
    position: absolute;
    left: 29px; top: 112px;
    width: 345px;
    font-size: 15px;
    line-height: 20.5px;
  }
  .letter__cta {
    position: absolute;
    left: 29px; top: 202px;
    width: 345px;
    font-weight: 700;
    font-size: 14px;
    line-height: 18px;
  }
  .divider {
    position: absolute;
    left: 29px; top: 244px;
    width: 330px; height: 2px;
    background: var(--gold);
  }
  .fine-print {
    position: absolute;
    left: 29px; top: 258px;
    width: 338px;
    font-size: 8.6px;
    line-height: 15px;
  }
  .back-call {
    position: absolute;
    left: 29px; top: 404px;
    display: flex;
    align-items: center;
    gap: 14px;
  }
  .back-call .call-tag {
    font-size: 15px;
    letter-spacing: 2px;
    line-height: 26px;
    width: 67px;
    text-align: center;
  }
  .back-call .call-number { font-size: 27px; line-height: 34px; }

  .stamp-box {
    position: absolute;
    left: 584px; top: 29px;
    width: 77px; height: 79px;
    border: 1px solid #8a8a8a;
  }
  .address-line {
    position: absolute;
    left: 447px;
    width: 214px; height: 1px;
    background: var(--rule);
  }
  .address-line--1 { top: 292px; }
  .address-line--2 { top: 323px; }
  .address-line--3 { top: 354px; }
  .address-line--4 { top: 383px; }
</style>
</head>
<body>

  <section class="postcard postcard--front" aria-label="Postcard front">
    <svg class="card-art" viewBox="0 0 675 482" aria-hidden="true">
      <defs>
        <linearGradient id="gold-band" x1="0" y1="0" x2="1" y2="0">
          <stop offset="0" stop-color="#b07e1c"/>
          <stop offset="0.45" stop-color="#e6c15c"/>
          <stop offset="1" stop-color="#b8861f"/>
        </linearGradient>
      </defs>
      <rect x="0" y="0" width="675" height="200" fill="url(#gold-band)"/>
      <path d="M0,184 Q190,160 374,170 L374,180 Q190,172 0,196 Z" fill="#13284a"/>
      <path d="M0,196 Q190,172 374,180 L374,482 L0,482 Z" fill="#ffffff"/>
    </svg>

    <div class="hero-photo" role="img" aria-label="Photo of a smiling young couple, woman hugging man from behind"></div>

    <div class="headline">
      <div class="headline__main">CASH OUT<br>EQUITY LOAN</div>
      <div class="headline__sub">ON YOUR INVESTMENT PROPERTY</div>
    </div>

    <ul class="benefits">
      <li><svg viewBox="0 0 12 12"><path d="M1.5,6.5 L4.5,9.5 L10.5,2" fill="none" stroke="#d3202a" stroke-width="1.8"/></svg>Loan based on your equity</li>
      <li><svg viewBox="0 0 12 12"><path d="M1.5,6.5 L4.5,9.5 L10.5,2" fill="none" stroke="#d3202a" stroke-width="1.8"/></svg>Fast choice</li>
      <li><svg viewBox="0 0 12 12"><path d="M1.5,6.5 L4.5,9.5 L10.5,2" fill="none" stroke="#d3202a" stroke-width="1.8"/></svg>No income qualifying</li>
      <li><svg viewBox="0 0 12 12"><path d="M1.5,6.5 L4.5,9.5 L10.5,2" fill="none" stroke="#d3202a" stroke-width="1.8"/></svg>Competitive rates</li>
      <li><svg viewBox="0 0 12 12"><path d="M1.5,6.5 L4.5,9.5 L10.5,2" fill="none" stroke="#d3202a" stroke-width="1.8"/></svg>Not based on credit scores</li>
    </ul>

    <div class="nmls">NMLS #481562</div>
    <div class="brand">
      <span class="brand__mark"></span>
      <span class="brand__name">Crestline Home<br>Lending, Inc.</span>
    </div>

    <div class="call-bar">
      <span class="call-tag">CALL</span>
      <span class="call-number">800-555-0147</span>
    </div>
  </section>

  <section class="postcard postcard--back" aria-label="Postcard back">
    <svg class="card-art" viewBox="0 0 675 471" aria-hidden="true">
      <defs>
        <linearGradient id="gold-arc" x1="0" y1="0" x2="0" y2="1">
          <stop offset="0" stop-color="#e6c15c"/>
          <stop offset="0.5" stop-color="#b8861f"/>
          <stop offset="1" stop-color="#e0b64e"/>
        </linearGradient>
      </defs>
      <rect x="0" y="374" width="420" height="97" fill="#13284a"/>
      <path d="M385,0 Q467,235 360,471 L675,471 L675,0 Z" fill="#ffffff"/>
      <path d="M335,0 Q455,235 335,471 L360,471 Q467,235 385,0 Z" fill="url(#gold-arc)"/>
    </svg>

    <div class="brand">
      <span class="brand__mark"></span>
      <span class="brand__name">Crestline Home<br>Lending, Inc.</span>
    </div>

    <p class="letter">I am please to inform you that an equity bared loan is available for your investment property. This no qualifying loan is possible simply due to the equity you have.</p>
    <p class="letter__cta">Please call 800-555-0147 for a quote or<br>email info@crestline.loan</p>
    <div class="divider"></div>
    <p class="fine-print">*Loan is subject to confirmation of equity and is for income property, investment property, rental property or business purpose, other restrictions and conditions apply. Please call for complete program requirements and details. Crestline Home Lending, Inc. 2200 Orchard Way, Suite 4, Lakeview CA 90000. Dana Ellis, CA Dept of Real Estate – Real Estate Broker Lic. #01234567 NMLS #557310 CA Dept. of Real Estate Corporate Lic. #01765432, NMLS #481562.</p>

    <div class="back-call">
      <span class="call-tag">CALL</span>
      <span class="call-number">800-555-0147</span>
    </div>

    <div class="stamp-box"></div>
    <div class="address-line address-line--1"></div>
    <div class="address-line address-line--2"></div>
    <div class="address-line address-line--3"></div>
    <div class="address-line address-line--4"></div>
  </section>

</body>
</html>
```